Business card design needed

Want the logo on a medium blue background and a nice funky design. I have my own gym and run one on one personal training and nutrition sessions. want it to look lively.
Updates

Please note I requested my logo on a blue background 

PLEASE NOTE: I already have a logo. It is attached to the order!!

Target Market(s)

over 55s

Industry/Entity Type

Nutrition

Contact Information for Business Card

Front of card : Logo ( on blue background )
Keldra Ashby
Nutrition & Fitness Coach for Seniors
Private gym at : 17 Tindal Crescent, Wembury, Perth, WA 6172
Mob : 0418372651
Email : keldraashby@frelmo.com
"For Seniors by a Senior"

Back of card
B.A. ( Soc.)
Dip. Ed. (Sec.)
Wellness Coach
Cert 4 Personal Trainer
Cert. Nutritition
MOVE ON Facilitator
Ageing Boldly Moving Freely Facilitator
NLP Master

```html
<!DOCTYPE html>
<html lang="en">
<head>
<meta charset="utf-8">
<title>Keldra Ashby Nutrition &amp; Fitness – Business Card</title>
<link rel="stylesheet" href="https://fonts.googleapis.com/css2?family=Cormorant+Garamond:ital,wght@1,600&family=Arimo&family=Tinos&display=swap">
<style>
  :root {
    --page: #ffffff;
    --card-white: #ffffff;
    --card-edge: #2a2a2a;
    --sky: #9fd9ea;
    --teal: #2393a8;
    --ink-grey: #555555;
    --ink-navy: #0a1a80;
    --link-blue: #1010e0;
    --brand-blue: #1f6fe0;
    --dot-light: #6fb4ff;
    --dot-dark: #0a55d8;
  }
  html, body {
    margin: 0;
    padding: 0;
    width: 1200px;
    height: 376px;
    overflow: hidden;
    background: var(--page);
  }
  .canvas {
    position: relative;
    width: 1200px;
    height: 376px;
  }
  .card {
    position: absolute;
    top: 14px;
    width: 562px;
    height: 330px;
    background: var(--card-white);
    outline: 1px solid var(--card-edge);
    overflow: hidden;
  }
  .card--front { left: 12px; }
  .card--back { left: 624px; }
  .card__backdrop {
    position: absolute;
    inset: 0;
  }
  .script {
    font-family: "Cormorant Garamond", "Palatino Linotype", serif;
    font-style: italic;
    font-weight: 600;
    position: absolute;
    margin: 0;
    white-space: nowrap;
    color: var(--ink-grey);
    line-height: 1.2;
  }
  .business-name { left: 182px; top: 10px; font-size: 29px; }
  .tagline-role { left: 400px; top: 46px; font-size: 23px; color: var(--ink-navy); }
  .motto { left: 246px; top: 295px; font-size: 23px; }
  .contact {
    position: absolute;
    left: 324px;
    top: 174px;
    font-family: "Arimo", Arial, sans-serif;
    font-size: 15px;
    line-height: 18px;
    color: var(--ink-navy);
  }
  .contact__row { display: flex; }
  .contact__label { width: 109px; white-space: nowrap; }
  .contact__value { color: var(--ink-grey); }
  .contact__email { color: var(--link-blue); }
  .brand-name {
    position: absolute;
    left: 48px;
    top: 198px;
    width: 124px;
    text-align: center;
    font-family: "Tinos", "Times New Roman", serif;
    font-size: 23px;
    color: var(--ink-grey);
  }
  .credentials {
    position: absolute;
    left: 0;
    top: 64px;
    margin: 0;
    padding: 0;
    list-style: none;
  }
  .credentials li {
    font-family: "Cormorant Garamond", "Palatino Linotype", serif;
    font-style: italic;
    font-weight: 600;
    font-size: 23px;
    line-height: 28px;
    color: var(--ink-grey);
    white-space: nowrap;
  }
</style>
</head>
<body>
<div class="canvas">

  <section class="card card--front" aria-label="Front of business card">
    <svg class="card__backdrop" width="562" height="330" viewBox="0 0 562 330" aria-hidden="true">
      <defs>
        <radialGradient id="dotShade" cx="35%" cy="35%" r="70%">
          <stop offset="0" stop-color="var(--dot-light)"/>
          <stop offset="1" stop-color="var(--dot-dark)"/>
        </radialGradient>
      </defs>
      <path d="M150,0 Q265,165 152,330 L562,330 L562,0 Z" fill="var(--sky)"/>
      <path d="M150,-2 Q265,165 152,332" fill="none" stroke="var(--teal)" stroke-width="6"/>
      <g fill="url(#dotShade)">
        <circle cx="18" cy="105" r="10"/>
        <circle cx="18" cy="129" r="10"/>
        <circle cx="18" cy="153" r="10"/>
        <circle cx="18" cy="177" r="10"/>
        <circle cx="18" cy="201" r="10"/>
        <circle cx="18" cy="225" r="10"/>
      </g>
      <circle cx="110" cy="156" r="70" fill="var(--brand-blue)"/>
    </svg>
    <div class="brand-name">Keldra</div>

    <h1 class="script business-name">Keldra Ashby Nutrition &amp; Fitness</h1>
    <p class="script tagline-role">Coach for Seniors</p>

    <div class="contact">
      <div class="contact__row"><span class="contact__label">Private gym at :</span><span class="contact__value">17 Tindal Crescent,<br>Wembury, Perth,<br>WA 6172</span></div>
      <div class="contact__row"><span class="contact__label">Mob : <span class="contact__value">0418372651</span></span></div>
      <div class="contact__row"><span>Email : <span class="contact__email">keldraashby@frelmo.com</span></span></div>
    </div>

    <p class="script motto">For Seniors by a Senior..!</p>
  </section>

  <section class="card card--back" aria-label="Back of business card">
    <svg class="card__backdrop" width="562" height="330" viewBox="0 0 562 330" aria-hidden="true">
      <defs>
        <radialGradient id="dotShadeBack" cx="35%" cy="35%" r="70%">
          <stop offset="0" stop-color="var(--dot-light)"/>
          <stop offset="1" stop-color="var(--dot-dark)"/>
        </radialGradient>
      </defs>
      <path d="M150,0 Q265,165 152,330 L562,330 L562,0 Z" fill="var(--sky)"/>
      <path d="M150,-2 Q265,165 152,332" fill="none" stroke="var(--teal)" stroke-width="6"/>
      <g fill="url(#dotShadeBack)">
        <circle cx="18" cy="105" r="10"/>
        <circle cx="18" cy="129" r="10"/>
        <circle cx="18" cy="153" r="10"/>
        <circle cx="18" cy="177" r="10"/>
        <circle cx="18" cy="201" r="10"/>
        <circle cx="18" cy="225" r="10"/>
      </g>
      <circle cx="110" cy="156" r="70" fill="var(--brand-blue)"/>
    </svg>
    <div class="brand-name">Keldra</div>

    <ul class="credentials">
      <li style="margin-left:206px">B.A. ( Soc.) Dip. Ed. (Sec.)</li>
      <li style="margin-left:217px">Wellness Coach Certified for</li>
      <li style="margin-left:227px">Personal Trainer</li>
      <li style="margin-left:227px">Certified Nutritition</li>
      <li style="margin-left:227px">MOVE ON Facilitator</li>
      <li style="margin-left:222px">Ageing Boldly Moving Freely</li>
      <li style="margin-left:212px">Facilitator NLP Master</li>
    </ul>
  </section>

</div>
</body>
</html>
```